Spring Frenzy Themed Postcard Promoting Preventative Maintenance for Professional Cleaning Equipment

We need a postcard design for a company that sells and maintains professional cleaning equipment. We deal with farmers, trucking companies and construction companies that use our equipment to keep their trucks, tractors and barns clean. We need the card to be themed after the UCLB Spring Frenzy (http://www.uclb-hoops.example/spring-frenzy).
some key ideas are modern, sleek, eye catching, basket-ball themed. Nothing comical or childish. This is geared toward 30-50 year old males.

Target Market(s)

Agricultural and industrial professionals

Industry/Entity Type

Construction

Font styles to use
Serif
Sans Serif

Requirements
Must have
• Basketball theme

```html
<!DOCTYPE html>
<html lang="en">
<head>
<meta charset="utf-8">
<title>Spring Frenzy at KTW – Pressure Washer Maintenance</title>
<link rel="stylesheet" href="https://fonts.googleapis.com/css2?family=Open+Sans:wght@400;600;700;800&family=Oswald:wght@700&display=swap">
<style>
  :root {
    --ink-black: #050505;
    --spot-grey: #2a2a2a;
    --text-white: #ffffff;
    --burst-red: #d7141a;
    --floor-light: #b77a3e;
    --floor-dark: #5a3414;
    --steel-dark: #1d1f22;
    --steel-light: #6b6f75;
    --badge-steel: #3b4450;
  }
  * { margin: 0; padding: 0; box-sizing: border-box; }
  html, body { width: 1200px; height: 936px; overflow: hidden; background: var(--ink-black); }
  .postcard {
    position: relative;
    width: 1200px;
    height: 936px;
    overflow: hidden;
    font-family: "Open Sans", Arial, sans-serif;
    color: var(--text-white);
    background: radial-gradient(ellipse 60% 55% at 50% 40%, var(--spot-grey) 0%, var(--ink-black) 75%);
  }
  .court-floor {
    position: absolute;
    left: 0; right: 0; bottom: 0;
    height: 250px;
    background: linear-gradient(180deg, rgba(5,5,5,1) 0%, var(--floor-dark) 40%, var(--floor-light) 100%);
  }
  .headline {
    position: absolute;
    left: 36px; top: 30px;
    font-size: 38px;
    font-weight: 700;
    letter-spacing: 0.5px;
  }
  .body-copy {
    position: absolute;
    left: 36px; top: 112px;
    width: 780px;
    font-size: 31px;
    line-height: 41px;
    font-weight: 400;
  }
  .body-copy p + p { margin-top: 41px; }
  .phone {
    position: absolute;
    left: 120px; top: 436px;
    font-size: 70px;
    font-weight: 400;
    letter-spacing: 1px;
  }
  .offer-burst {
    position: absolute;
    left: 800px; top: 12px;
    width: 380px; height: 380px;
  }
  .offer-burst svg { position: absolute; inset: 0; width: 100%; height: 100%; }
  .offer-text {
    position: absolute;
    inset: 0;
    display: flex;
    align-items: center;
    justify-content: center;
    text-align: center;
    font-size: 33px;
    line-height: 40px;
    font-weight: 400;
    padding-top: 6px;
  }
  .event-badge {
    position: absolute;
    left: 18px; top: 560px;
    width: 570px; height: 340px;
  }
  .company-mark {
    position: absolute;
    left: 0; top: 20px;
    display: flex;
    align-items: center;
    gap: 10px;
    font-size: 26px;
    font-weight: 800;
    color: var(--text-white);
  }
  .company-mark .dot {
    width: 30px; height: 30px;
    border-radius: 50%;
    background: var(--burst-red);
  }
  .event-title {
    position: absolute;
    left: 140px; top: 60px;
    font-family: "Oswald", "Arial Narrow", sans-serif;
    font-weight: 700;
    font-size: 108px;
    line-height: 104px;
    color: var(--text-white);
    text-transform: uppercase;
  }
  .event-dates {
    position: absolute;
    left: 160px; top: 278px;
    width: 380px; height: 56px;
    background: var(--text-white);
    color: var(--ink-black);
    border: 3px solid var(--badge-steel);
    font-size: 28px;
    font-weight: 600;
    display: flex;
    align-items: center;
    justify-content: center;
  }
  .washer-photo {
    position: absolute;
    left: 804px; top: 450px;
    width: 340px; height: 450px;
    border-radius: 10px;
    background: linear-gradient(135deg, var(--steel-light) 0%, var(--steel-dark) 55%, #0d0e10 100%);
  }
</style>
</head>
<body>
<main class="postcard">
  <div class="court-floor" role="img" aria-label="Polished wooden basketball court floor"></div>

  <h1 class="headline">SPRING FRENZY IS HERE AT KTW!</h1>

  <div class="body-copy">
    <p>Instead of polished wood, your shop<br>is our court and our goal is to assist you in<br>making spring clean-up a slam dunk!</p>
    <p>Now is the time to get your pressure<br>washer in game-ready condition.</p>
    <p>Call today to schedule a preventative maintenance.</p>
  </div>

  <div class="phone">555.014.2876</div>

  <div class="offer-burst">
    <svg viewBox="-100 -100 200 200" aria-hidden="true">
      <polygon fill="var(--burst-red)" points="100,0 86.3,17.2 92.4,38.3 73.2,48.9 70.7,70.7 48.9,73.2 38.3,92.4 17.2,86.3 0,100 -17.2,86.3 -38.3,92.4 -48.9,73.2 -70.7,70.7 -73.2,48.9 -92.4,38.3 -86.3,17.2 -100,0 -86.3,-17.2 -92.4,-38.3 -73.2,-48.9 -70.7,-70.7 -48.9,-73.2 -38.3,-92.4 -17.2,-86.3 0,-100 17.2,-86.3 38.3,-92.4 48.9,-73.2 70.7,-70.7 73.2,-48.9 92.4,-38.3 86.3,-17.2"/>
    </svg>
    <div class="offer-text">Pressure<br>Washer<br>Preventative<br>Maintenance<br>package<br>$97 or less!</div>
  </div>

  <div class="event-badge">
    <div class="company-mark"><span class="dot"></span>KTW GROUP</div>
    <div class="event-title">Spring<br>Frenzy</div>
    <div class="event-dates">UNTIL March 31, 2015</div>
  </div>

  <div class="washer-photo" role="img" aria-label="Photo of a stainless steel Northvale hot water pressure washer"></div>
</main>
</body>
</html>
```